International IT business needs website revamp.

Velmont Limited would like their current website (www.velmontlimited-example.com) to be revamped/modernized to reflect up-to-date goods and services. Currently, Velmont is offering a conversational AI workflow platform for both enterprise clients and as a DIY solution for SMBs. This platform is called tqAgent and allows organizations to automate simple and repetitive workflows to drive their operational efficiency. In addition to the solution offering, Velmont Limited also provides professional IT services. With that said, please use www.velmontlimited-example.com and www.tqagent-example.ai for reference of current logos and colourways desired. Furthermore, refer to the attached PDF for a general idea of what to include in the site. The final design should be easy to navigate, clear, concise, and emphasize tqAgent as a solution for enterprise clients (while redirecting SMBs to the tqAgent website) looking to automate workflow processes/kickstart their digital transformation journey.

```html
<!DOCTYPE html>
<html lang="en">
<head>
<meta charset="utf-8">
<title>Velmont Limited</title>
<link href="https://fonts.googleapis.com/css2?family=Roboto:wght@400;500;700;900&family=Roboto+Condensed:wght@700&display=swap" rel="stylesheet">
<style>
:root{
  --green:#7ab648;
  --ink:#222;
  --text:#555;
  --partner:#c4c4c4;
  --client:#2d4f86;
  --panel:#f4f4f4;
  --white:#fff;
}
*{margin:0;padding:0;box-sizing:border-box}
html,body{width:1200px;height:3408px;overflow:hidden}
body{position:relative;font-family:'Roboto',sans-serif;color:var(--text);background:var(--white)}
.abs{position:absolute}
.topbar{left:0;top:0;width:1200px;height:36px;background:var(--green);color:#fff;font-size:14px}
.topbar .contact{left:66px;top:9px;display:flex;gap:22px;align-items:center}
.topbar .contact span{display:flex;align-items:center;gap:8px}
.topbar .social{right:66px;top:9px;display:flex;gap:10px;font-size:10px}
.topbar .social span{border:1px solid #fff;padding:1px 3px}
.nav{left:0;top:36px;width:1200px;height:75px;background:#fff}
.wordmark{font-size:24px;font-weight:500;color:var(--ink);letter-spacing:1px;white-space:nowrap}
.nav .wordmark{left:87px;top:22px}
.menu{left:528px;top:23px;display:flex;gap:40px;font-size:15px;font-weight:500;color:var(--ink)}
.menu .active{color:var(--green)}
.search{left:1096px;top:26px}
.hero{left:0;top:111px;width:1200px;height:638px;background:radial-gradient(ellipse at 50% 45%,#4a5663 0%,#1e2328 45%,#0a0b0c 80%)}
.hero h1{position:absolute;left:0;width:1200px;text-align:center;font-family:'Roboto Condensed',sans-serif;font-size:60px;line-height:1}
.hero .l1{top:255px;color:#fff}
.hero .l2{top:330px;color:var(--green)}
.dots{left:567px;top:600px;display:flex;gap:14px}
.dots i{width:12px;height:12px;border-radius:50%;background:#fff}
.dots i:first-child{background:var(--green)}
.about{left:0;top:749px;width:1200px;height:540px;background:var(--panel)}
.h2{font-family:'Roboto Condensed',sans-serif;font-size:44px;color:var(--green);font-weight:700}
.about .h2{position:absolute;left:66px;top:70px}
.about p{position:absolute;left:66px;width:580px;font-size:13.5px;line-height:26.5px}
.btn{left:66px;top:417px;width:168px;height:47px;border:3px solid var(--green);color:var(--green);font-size:15px;font-weight:500;display:flex;align-items:center;justify-content:center}
.about-photo{left:630px;top:0;width:570px;height:540px;background:linear-gradient(135deg,#d9d6d2,#8d8c8e 55%,#3a3d44);clip-path:polygon(190px 0,570px 0,570px 540px,250px 540px,0 230px)}
.center{left:0;width:1200px;text-align:center}
.t-photo{left:126px;top:1473px;width:291px;height:357px;background:#fff;box-shadow:0 0 4px rgba(0,0,0,.25);padding:10px}
.t-photo div{width:100%;height:100%;background:linear-gradient(180deg,#f3f3f3,#cfd8e2 60%,#b9c7d6)}
.t-card{left:388px;top:1594px;width:645px;height:257px;background:#fff;border-left:14px solid var(--green);box-shadow:0 0 5px rgba(0,0,0,.2)}
.t-card h3{text-align:center;color:var(--green);font-size:17px;font-weight:500;margin-top:28px}
.t-card p{margin:22px 30px 0 16px;font-size:13.5px;line-height:26.3px}
.quote{left:1020px;top:1466px;font-weight:900;font-size:78px;color:var(--green);line-height:1}
.sq{width:45px;height:45px;background:var(--green);display:flex;align-items:center;justify-content:center}
.video{top:2015px;width:330px;height:296px;background:linear-gradient(160deg,#3b4048,#15181c)}
.video.v2{background:linear-gradient(160deg,#1c2a38,#6a7683 60%,#2a3440)}
.video.v3{background:linear-gradient(160deg,#0d1e2a,#1e6f86 60%,#0b2a36)}
.vbar{position:absolute;left:12px;top:10px;right:12px;display:flex;align-items:center;gap:12px;color:#fff;font-size:16px}
.vbar .av{width:30px;height:30px;border-radius:50%;background:var(--green);display:flex;align-items:center;justify-content:center;font-weight:700}
.play{position:absolute;left:141px;top:124px;width:48px;height:48px;border-radius:50%;background:rgba(0,0,0,.55);display:flex;align-items:center;justify-content:center}
.clients-box{left:65px;top:2518px;width:1070px;height:182px;border:1px solid #e5e5e5;box-shadow:0 0 3px rgba(0,0,0,.08)}
.client-row{left:90px;top:0;width:890px;height:180px;display:flex;align-items:center;justify-content:space-around}
.client{font-weight:900;font-size:36px;color:var(--client);white-space:nowrap}
.partners{left:0;top:2882px;width:1200px;height:165px;background:#f4f4f4;border-top:2px solid #e8e8e8;display:flex;align-items:center;justify-content:space-around}
.partner{font-size:50px;font-weight:700;color:var(--partner);white-space:nowrap}
.footer{left:0;top:3047px;width:1200px;height:361px;background:var(--green);color:#fff}
.footer .wordmark{position:absolute;left:87px;top:70px;color:#fff;font-size:48px;font-weight:400}
.fsocial{left:95px;top:182px;display:flex;gap:18px;font-size:12px;font-weight:500}
.fsocial span{width:34px;height:34px;border:2px solid #fff;display:flex;align-items:center;justify-content:center}
.fcol{top:36px;font-size:15px;font-weight:500}
.fcol h4{font-size:17px;font-weight:700;margin-bottom:18px}
.fcol li{list-style:none;height:38px;white-space:nowrap}
.fcol.contact{font-size:14px}
.frule{left:66px;top:3334px;width:1068px;height:1px;background:#fff}
.copy{left:0;top:3362px;width:1200px;text-align:center;color:#fff;font-size:15px}
</style>
</head>
<body>

<div class="abs topbar">
  <div class="abs contact">
    <span><svg width="14" height="11" viewBox="0 0 14 11"><rect width="14" height="11" fill="#fff"/><path d="M0 0l7 6 7-6" stroke="#7ab648" fill="none" stroke-width="1.5"/></svg>info@velmontlimited-example.com</span>
    <span><svg width="13" height="13" viewBox="0 0 24 24"><path fill="#fff" d="M6.6 10.8a15 15 0 0 0 6.6 6.6l2.2-2.2c.3-.3.7-.4 1-.2 1.1.4 2.3.6 3.6.6.6 0 1 .4 1 1V20c0 .6-.4 1-1 1A17 17 0 0 1 3 4c0-.6.4-1 1-1h3.5c.6 0 1 .4 1 1 0 1.3.2 2.5.6 3.6.1.3 0 .7-.2 1z"/></svg>(555) 010-2244</span>
  </div>
  <div class="abs social"><span>Chirp</span><span>Folio</span><span>Linkr</span><span>Gather</span></div>
</div>

<header class="abs nav">
  <div class="abs wordmark">VELMONT</div>
  <nav class="abs menu"><span class="active">Home</span><span>Solutions</span><span>Services</span><span>Request a Demo</span><span>About Us</span></nav>
  <svg class="abs search" width="16" height="16" viewBox="0 0 16 16"><circle cx="6.5" cy="6.5" r="5" stroke="#222" stroke-width="2" fill="none"/><path d="M10 10l5 5" stroke="#222" stroke-width="2.4"/></svg>
</header>

<section class="abs hero" role="img" aria-label="Hand holding a glowing network of gears against a dark background">
  <h1 class="l1">WELCOME FOR</h1>
  <h1 class="l2">VELMONT COMPANY</h1>
  <div class="abs dots"><i></i><i></i><i></i></div>
</section>

<section class="abs about">
  <h2 class="h2">About Us</h2>
  <p style="top:136px">Since 2011, the Velmont team has been providing professional IT services for major Canadian corporations operating in the telecommunications and financial sectors. As such, our team is highly skilled in technology integration, legacy modernization, system architecture design, application development, quality assurance, project management and more!</p>
  <p style="top:250px">As of 2017, the Velmont team has developed and launched tqAgent, a conversational workflow platform powered by AI and ML, into production. Our vision for tqAgent is to drive the operational economy, efficiency, and effectiveness of any organization by automating simple and repetitive workflows.</p>
  <div class="abs btn">READ MORE</div>
  <div class="abs about-photo" role="img" aria-label="Smiling businesswoman with arms crossed in an office with colleagues"></div>
</section>

<h2 class="abs h2 center" style="top:1365px">Testimonials</h2>
<div class="abs t-photo"><div role="img" aria-label="Portrait of a smiling businessman with arms crossed"></div></div>
<div class="abs quote">”</div>
<div class="abs sq" style="left:1033px;top:1551px"><svg width="14" height="18" viewBox="0 0 14 18"><path d="M3 2l8 7-8 7" stroke="#fff" stroke-width="3" fill="none"/></svg></div>
<div class="abs t-card">
  <h3>Civic Travel Office</h3>
  <p>“Naturally, the Civic Travel Office website receives thousands of visitors a day. As a result, we noticed the need to automate simple and repetitive questions to provide quick, on-demand assistance while maximizing our worker productivity without compromising costs. Thus, we enlisted Velmont Limited and their tqAgent solution to accomplish the task. Since launching the Civic Travel Office bot in Q4, 2019, we have achieved over 75% of inquiries being automatically answered successfully!”</p>
</div>
<div class="abs sq" style="left:990px;top:1596px;width:43px;height:43px"><svg width="14" height="18" viewBox="0 0 14 18"><path d="M11 2l-8 7 8 7" stroke="#fff" stroke-width="3" fill="none"/></svg></div>

<h2 class="abs h2 center" style="top:1928px">Promotional Videos</h2>
<svg class="abs" style="left:64px;top:2142px" width="16" height="24" viewBox="0 0 16 24"><path d="M13 2L3 12l10 10" stroke="#7ab648" stroke-width="3" fill="none"/></svg>
<svg class="abs" style="left:1118px;top:2142px" width="16" height="24" viewBox="0 0 16 24"><path d="M3 2l10 10L3 22" stroke="#7ab648" stroke-width="3" fill="none"/></svg>
<div class="abs video" style="left:95px" role="img" aria-label="Video thumbnail: business handshake in front of media screens">
  <div class="vbar"><span class="av">T</span>The QRS Solution</div>
  <div class="play"><svg width="18" height="20"><path d="M2 1l15 9-15 9z" fill="#fff"/></svg></div>
</div>
<div class="abs video v2" style="left:435px" role="img" aria-label="Video thumbnail: hand touching connected device icons">
  <div class="vbar"><span class="av">T</span>The QRS Solution</div>
  <div class="play"><svg width="18" height="20"><path d="M2 1l15 9-15 9z" fill="#fff"/></svg></div>
</div>
<div class="abs video v3" style="left:774px" role="img" aria-label="Video thumbnail: glowing hand with a rising growth arrow">
  <div class="vbar"><span class="av">T</span>The QRS Solution</div>
  <div class="play"><svg width="18" height="20"><path d="M2 1l15 9-15 9z" fill="#fff"/></svg></div>
</div>

<h2 class="abs h2 center" style="top:2388px">Our Clients</h2>
<p class="abs center" style="top:2477px;font-size:13.5px">Velmont’s current clientele consists of businesses from many sectors including Advertising, Financial and Telecommunication companies.</p>
<div class="abs clients-box">
  <svg class="abs" style="left:16px;top:79px" width="14" height="22" viewBox="0 0 14 22"><path d="M11 2L3 11l8 9" stroke="#7ab648" stroke-width="3" fill="none"/></svg>
  <div class="abs client-row">
    <span class="client">Brightline</span>
    <span class="client">Onyxa</span>
    <span class="client">Meridus</span>
    <span class="client">Roadsure</span>
  </div>
  <svg class="abs" style="left:1040px;top:79px" width="14" height="22" viewBox="0 0 14 22"><path d="M3 2l8 9-8 9" stroke="#7ab648" stroke-width="3" fill="none"/></svg>
</div>

<h2 class="abs h2 center" style="top:2775px">Our Partners</h2>
<div class="abs partners">
  <span class="partner">Solvex</span>
  <span class="partner">Intrix</span>
  <span class="partner">Amberon</span>
  <span class="partner">Northgate</span>
</div>

<footer class="abs footer">
  <div class="wordmark">VELMONT</div>
  <div class="abs fsocial"><span>Ch</span><span>Fo</span><span>Li</span><span>Ga</span></div>
  <div class="abs fcol" style="left:466px"><h4>Links</h4><ul><li>Home</li><li>Solutions</li><li>Services</li><li>Request a Demo</li><li>About Us</li></ul></div>
  <div class="abs fcol" style="left:668px"><h4>Address</h4><ul><li>1200 Example Avenue,</li><li>Unit 4 &amp; 5 Northfield,</li><li>ON Canada, A1B 2C3</li></ul></div>
  <div class="abs fcol contact" style="left:900px"><h4>Contact Us</h4><ul><li>✉&nbsp; info@velmontlimited-example.com</li><li>☎&nbsp; Phone: (555) 010-2244</li></ul></div>
</footer>
<div class="abs frule"></div>
<p class="abs copy">© 2020 Velmont Limited. All rights reserved.</p>

</body>
</html>
```